Bref créative
Brookstone Dental Group
trifold brochure and a glossy print ad for magazine back cover. I have attached references for both.
Health
Patients/general public
Maintain integrity of oak tree logo along with green color Trifold must be two colors only text of draft can be modified but basic info must remain the same-clean lines and simple if possible. Magazine ad can be multicolored.
Here is our logo in JPG format
Logo in EPS format

```html
<!DOCTYPE html>
<html lang="en">
<head>
<meta charset="utf-8">
<title>Brookstone Dental Group – Trifold Inside</title>
<link href="https://fonts.googleapis.com/css2?family=Arimo:ital,wght@0,400;0,700;1,400&family=Libre+Baskerville:wght@700&family=Pinyon+Script&display=swap" rel="stylesheet">
<style>
  :root{
    --green:#1f8a3a;
    --green-dark:#0f6a2c;
    --green-light:#8cc63f;
    --ink:#4a4a4a;
    --paper:#ffffff;
    --paper-shade:#eeeeee;
  }
  *{margin:0;padding:0;box-sizing:border-box}
  html,body{width:1200px;height:926px;overflow:hidden;background:var(--paper)}
  .brochure{position:relative;width:1200px;height:926px;overflow:hidden;
    background:linear-gradient(90deg,var(--paper) 0%,var(--paper-shade) 60%,var(--paper) 100%);
    font-family:"Arimo",Arial,sans-serif;color:var(--ink)}
  .panel{position:absolute;top:0;height:926px}
  .panel--left{left:0;width:400px;padding:52px 44px 0 42px}
  .panel--middle{left:400px;width:400px;padding:52px 20px 0 25px}
  .panel--right{left:800px;width:400px}
  .section-title{color:var(--green);font-weight:700;font-size:23px;line-height:28px}
  .subhead{font-style:italic;font-weight:400;font-size:19px;line-height:24px;margin-top:20px;color:var(--ink)}
  .body-copy{font-size:13.5px;line-height:17.5px;margin-top:14px}
  .block{margin-top:48px}
  .roster{list-style:none;font-size:13.5px;line-height:17.2px;margin-top:14px}
  .dept{margin-bottom:46px}
  .brand{position:absolute;left:0;right:0;top:62px;text-align:center}
  .brand-mark{display:block;width:130px;height:130px;margin:0 0 0 128px;background:var(--green)}
  .brand-name{margin-top:48px;margin-left:-10px;font-family:"Libre Baskerville",Georgia,serif;font-weight:700;
    color:var(--green);font-size:22px;line-height:26px;letter-spacing:.5px}
  .tagline{margin-top:36px;margin-left:90px;font-family:"Pinyon Script",cursive;color:var(--green);font-size:32px}
  .photo{position:absolute}
  .photo--family{left:400px;top:530px;width:350px;height:260px;border-radius:46% 54% 8% 8%/55% 55% 8% 8%;
    background:radial-gradient(ellipse at 50% 40%,#e8d2b8 0%,#c9ab88 45%,#e9ecef 100%)}
  .photo--smile{left:862px;top:437px;width:338px;height:320px;border-radius:50% 0 0 0/45% 0 0 0;
    background:radial-gradient(ellipse at 45% 45%,#e9c3a5 0%,#7a4a2e 55%,#f2f2f2 100%)}
  .band{position:absolute;left:0;top:690px;width:1200px;height:236px}
  .contact{position:absolute;left:400px;width:380px;top:818px;text-align:center;color:var(--paper);
    font-style:normal;font-weight:700;font-size:11.5px;line-height:18px}
  .contact .phone{font-size:12.5px;margin-top:4px}
</style>
</head>
<body>
<main class="brochure">

  <section class="panel panel--left">
    <h2 class="section-title">Community Service</h2>
    <h3 class="subhead">Office Tours and School Programs:</h3>
    <p class="body-copy">Brookstone Dental Group sponsors office tours to elementary and pre-school aged children to introduce the dental environment to children. This helps to familiarize the children with a dental office, making their dental visits more comfortable.</p>

    <div class="block">
      <h3 class="subhead">Bilingual Services</h3>
      <p class="body-copy">Several of our doctors speak more than one language. Translation is available for our Spanish, Portuguese, Greek, Arabic, Punjabi and Hindi speaking patients.</p>
    </div>

    <div class="block">
      <h3 class="subhead">Fees</h3>
      <p class="body-copy">We are members of many insurance plans and bill insurance companies for our patients. We also have several different payment options. All of our Doctors are members of the National Dental Alliance and the Western State Dental Council and are held to high standards.</p>
    </div>
  </section>

  <section class="panel panel--middle">
    <div class="dept">
      <h2 class="section-title">General Dentistry</h2>
      <ul class="roster">
        <li>Owen Carraway, DDS</li>
        <li>Lydia Fenmore, DDS</li>
        <li>Tobias Renwick, DDS</li>
        <li>Clara Voss, DDS</li>
        <li>Dale Ashby, DDS</li>
        <li>Kiran Mehta, DDS</li>
        <li>Priya Mehta, DDS</li>
      </ul>
    </div>
    <div class="dept">
      <h2 class="section-title">Pediatric Dentistry</h2>
      <ul class="roster">
        <li>Samir Haddad, DDS</li>
        <li>Nisha Patel, DDS</li>
      </ul>
    </div>
    <div class="dept">
      <h2 class="section-title">Oral &amp; Maxillofacial Surgery</h2>
      <ul class="roster">
        <li>Julian Voss, DMD</li>
      </ul>
    </div>
  </section>

  <section class="panel panel--right">
    <div class="brand">
      <span class="brand-mark"></span>
      <p class="brand-name">BROOKSTONE<br>DENTAL GROUP</p>
      <p class="tagline">Committed to excellence.</p>
    </div>
  </section>

  <div class="photo photo--family" role="img" aria-label="Photo of a smiling family of four lying together on the floor"></div>
  <div class="photo photo--smile" role="img" aria-label="Photo of a smiling woman with dark hair"></div>

  <svg class="band" viewBox="0 0 1200 236" preserveAspectRatio="none" aria-hidden="true">
    <defs>
      <linearGradient id="bandFill" x1="0" y1="0" x2="0" y2="1">
        <stop offset="0" stop-color="#2c9a43"/>
        <stop offset="1" stop-color="#0d5f27"/>
      </linearGradient>
    </defs>
    <path d="M0 40 C300 90 800 70 1200 10 L1200 236 L0 236 Z" fill="var(--green-light)"/>
    <path d="M0 58 C320 100 820 80 1200 26 L1200 236 L0 236 Z" fill="url(#bandFill)"/>
  </svg>

  <address class="contact">
    <div>2240 W. Alder Ave.</div>
    <div>Fairbrook, CA 95100</div>
    <div>www.brookstonedentalgroup.com</div>
    <div class="phone">555.014.2287</div>
  </address>

</main>
</body>
</html>
```